Medical Practice Business Card

we need a business card for our new medical ophthalmology practice based in Needham Massachusetts. we are looking for a simple , modern and elegant design.
the card needs to contain the following
1- the logo of our practice (please see attached file)
2- the name of the practice : "Silver Birch Vision Group"
3- Doctor's Name: Tobias Rendell MD PhD
4- Specialty: Board-Certified Vitreoretinal Surgeon
5- practice address: 87 Larkspur Ave, Suite 210, Alderbrook MA 02481
7- Office number: 617- 482 - 7730
8- fax number: 617- 391 - 2268
9- email: info@sbvisiongroup.example
10- website: www.sbvisiongroup.example

```html
<!DOCTYPE html>
<html lang="en">
<head>
<meta charset="utf-8">
<title>Silver Birch Vision Group – Business Card</title>
<link rel="stylesheet" href="https://fonts.googleapis.com/css2?family=Cinzel:wght@600&family=Montserrat:wght@400;500;600&display=swap">
<style>
  :root {
    --bg: #d9d9d9;
    --navy: #1b3a5f;
    --navy-ink: #1b2f52;
    --emboss: #2a5580;
    --cyan: #2aa7d9;
    --paper: #ffffff;
    --text: #27324a;
  }
  * { margin: 0; padding: 0; box-sizing: border-box; }
  html, body { width: 1200px; height: 900px; overflow: hidden; }
  body {
    background: var(--bg);
    display: flex;
    flex-direction: column;
    align-items: center;
    justify-content: center;
    gap: 48px;
    font-family: "Montserrat", Arial, sans-serif;
  }
  .card {
    width: 640px;
    height: 366px;
    position: relative;
    box-shadow: 0 10px 24px rgba(0,0,0,.18);
  }

  /* Back side */
  .card-back {
    background: var(--navy);
    border-bottom: 4px solid var(--cyan);
    display: flex;
    align-items: center;
    justify-content: center;
  }
  .brand-name {
    font-family: "Montserrat", Arial, sans-serif;
    font-weight: 600;
    white-space: nowrap;
  }
  .card-back .brand-name { color: var(--emboss); font-size: 32px; }

  /* Front side */
  .card-front {
    background: var(--paper);
    border-bottom: 4px solid var(--cyan);
  }
  .card-front .brand-name {
    position: absolute;
    right: 44px;
    top: 60px;
    color: var(--navy-ink);
    font-size: 22px;
  }

  .doctor {
    position: absolute;
    left: 44px;
    top: 148px;
  }
  .doctor-name {
    font-family: "Cinzel", Georgia, serif;
    font-weight: 600;
    font-size: 20px;
    color: var(--navy-ink);
  }
  .doctor-degree { color: var(--cyan); font-size: 14px; margin-left: 4px; }
  .doctor-title { font-size: 13px; color: var(--text); margin-top: 2px; }

  .divider {
    position: absolute;
    left: 44px;
    right: 44px;
    top: 205px;
    height: 1px;
    background: var(--cyan);
  }

  .contacts {
    position: absolute;
    left: 44px;
    top: 226px;
    list-style: none;
  }
  .contacts li {
    display: flex;
    align-items: center;
    gap: 10px;
    font-size: 14px;
    color: var(--text);
    line-height: 26px;
  }
  .contacts svg {
    width: 14px; height: 14px;
    fill: none;
    stroke: var(--cyan);
    stroke-width: 1.6;
    stroke-linecap: round;
    stroke-linejoin: round;
  }
  .address {
    position: absolute;
    right: 44px;
    top: 226px;
    text-align: right;
    font-size: 13px;
    line-height: 20px;
    color: var(--text);
    font-style: normal;
  }
</style>
</head>
<body>

  <section class="card card-back" aria-label="Card back">
    <span class="brand-name">Silver Birch Vision Group</span>
  </section>

  <section class="card card-front" aria-label="Card front">
    <span class="brand-name">Silver Birch Vision Group</span>

    <div class="doctor">
      <p class="doctor-name">Tobias Rendell <span class="doctor-degree">MD PhD</span></p>
      <p class="doctor-title">Board-Certified Vitreoretinal Surgeon</p>
    </div>

    <div class="divider"></div>

    <ul class="contacts">
      <li>
        <svg viewBox="0 0 16 16"><path d="M4 1.5l2.5 3-1.5 1.5a8 8 0 0 0 5 5l1.5-1.5 3 2.5-1.5 2.5C7 14.5 1.5 9 1.5 3z"/></svg>
        617- 482 - 7730
      </li>
      <li>
        <svg viewBox="0 0 16 16"><rect x="4" y="1.5" width="8" height="4"/><rect x="1.5" y="5.5" width="13" height="6" rx="1"/><rect x="4" y="9.5" width="8" height="5"/></svg>
        617- 391 - 2268
      </li>
      <li>
        <svg viewBox="0 0 16 16"><rect x="1.5" y="3.5" width="13" height="9" rx="1"/><path d="M1.5 4l6.5 5 6.5-5"/></svg>
        info@sbvisiongroup.example
      </li>
      <li>
        <svg viewBox="0 0 16 16"><circle cx="8" cy="8" r="6.5"/><path d="M1.5 8h13M8 1.5c2 2 2 11 0 13M8 1.5c-2 2-2 11 0 13"/></svg>
        www.sbvisiongroup.example
      </li>
    </ul>

    <address class="address">
      Silver Birch Vision Group<br>
      87 Larkspur Ave, Suite 210,<br>
      Alderbrook MA 02481
    </address>
  </section>

</body>
</html>
```